Project Harbour 2

A business card with the following details

Rex Fenwright
Consultant/Speaker/Trainer

The Velvo Quarter (Insert Logo)
Notes and Insight for Brand Builders
www.velvoquarter.net

Rex.Fenwright@velvoquarter.net
+61 418 592 076

Target Market(s)

Small and Medium sized business owners
Brand marketers

Industry/Entity Type

Business

Requirements
Must have
• Utilise The Velvo Quarter Logo and colour scheme
Nice to have
• More male than female in outlook.
Have a connnected feel to it and a link to a precinct good too.
Bold and simple design the ideal

```html
<!DOCTYPE html>
<html lang="en">
<head>
<meta charset="utf-8">
<title>The Velvo Quarter – Business Card</title>
<link rel="stylesheet" href="https://fonts.googleapis.com/css2?family=Lato:wght@300;400;700&display=swap">
<style>
  :root {
    --navy: #1f4e79;
    --aqua: #4aa8c4;
    --ink: #4a4a4a;
    --paper: #f4f4f2;
    --backdrop: #d9d9d9;
  }
  * { box-sizing: border-box; margin: 0; padding: 0; }
  html, body {
    width: 1200px;
    height: 900px;
    overflow: hidden;
    background: var(--backdrop);
    font-family: "Lato", sans-serif;
  }
  .canvas {
    position: relative;
    width: 1200px;
    height: 900px;
  }
  .card {
    position: absolute;
    width: 640px;
    height: 366px;
    background: var(--paper);
    box-shadow: 0 6px 18px rgba(0,0,0,0.18);
    overflow: hidden;
  }

  /* Front of card */
  .card--front {
    left: 280px;
    top: 50px;
    display: flex;
    flex-direction: column;
    align-items: center;
    justify-content: center;
    gap: 18px;
  }
  .brand {
    display: flex;
    align-items: center;
    gap: 16px;
  }
  .brand__dot {
    width: 40px;
    height: 40px;
    border-radius: 50%;
    background: var(--navy);
  }
  .brand__name {
    font-size: 46px;
    font-weight: 700;
    color: var(--navy);
    letter-spacing: -0.5px;
    white-space: nowrap;
  }
  .tagline {
    font-size: 19px;
    font-weight: 400;
    color: var(--aqua);
    letter-spacing: 4px;
    white-space: nowrap;
  }

  /* Back of card */
  .card--back {
    left: 280px;
    top: 480px;
  }
  .back__band {
    position: absolute;
    left: 0;
    top: 0;
    width: 210px;
    height: 100%;
  }
  .contact {
    position: absolute;
    left: 250px;
    top: 52px;
    width: 360px;
  }
  .contact__name {
    font-size: 28px;
    font-weight: 400;
    color: var(--navy);
    letter-spacing: 0.5px;
    text-transform: uppercase;
    white-space: nowrap;
  }
  .contact__role {
    margin-top: 4px;
    font-size: 17px;
    color: var(--ink);
  }
  .contact__rule {
    margin: 14px 0 20px;
    height: 2px;
    background: var(--navy);
  }
  .contact__line {
    font-size: 18px;
    color: var(--ink);
    line-height: 1.3;
    white-space: nowrap;
  }
  .contact__web {
    margin-top: 12px;
    font-size: 18px;
    font-weight: 700;
    color: var(--ink);
    white-space: nowrap;
  }
  .social {
    display: flex;
    gap: 10px;
    margin-top: 16px;
  }
  .social__tile {
    width: 32px;
    height: 32px;
    border-radius: 3px;
    background: var(--navy);
  }
  .social__tile:nth-child(even) { background: var(--aqua); }
</style>
</head>
<body>
<main class="canvas">

  <section class="card card--front" aria-label="Card front">
    <div class="brand">
      <span class="brand__dot"></span>
      <span class="brand__name">The Velvo Quarter</span>
    </div>
    <p class="tagline">Notes and Insight for Brand Builders</p>
  </section>

  <section class="card card--back" aria-label="Card back">
    <svg class="back__band" viewBox="0 0 210 366" preserveAspectRatio="none" aria-hidden="true">
      <path d="M0 0 H150 Q210 183 150 366 H0 Z" fill="var(--navy)"/>
    </svg>
    <div class="contact">
      <h1 class="contact__name">Rex Fenwright</h1>
      <p class="contact__role">Consultant/Speaker/Trainer</p>
      <div class="contact__rule"></div>
      <p class="contact__line">+61 418 592 076</p>
      <p class="contact__line">Rex.Fenwright@velvoquarter.net</p>
      <p class="contact__web">www.velvoquarter.net</p>
      <div class="social" aria-label="Social profiles">
        <span class="social__tile"></span>
        <span class="social__tile"></span>
        <span class="social__tile"></span>
        <span class="social__tile"></span>
        <span class="social__tile"></span>
      </div>
    </div>
  </section>

</main>
</body>
</html>
```